Web design required

1-We need a web design for existing company based in New Zealand
2-We build residential house and light commercial
3-We has in-house designer which allow us can provide interior design
4-We modeling project before site construction, which enable both client and construction team to visually analysis whole project,

Target Market(s)

middle class residential house market
Ref: http://www.brambleworthbuilders.co.nz/

Industry/Entity Type

Construction Company

Number of Pages Required

1 page

Font styles to use
Sans Serif
Other font styles liked:
• Such as : Central Gothic or similar which has more design taste

Colors

Designer to choose colors to be used in the design.

Requirements
Must have
• Front sheet, contact information, sample project

```html
<!DOCTYPE html>
<html lang="en">
<head>
<meta charset="utf-8">
<title>Harbourline Homes</title>
<link rel="stylesheet" href="https://fonts.googleapis.com/css2?family=Raleway:wght@300;400;600;700;800&family=Open+Sans:ital,wght@0,400;0,600;0,700;1,400&display=swap">
<style>
:root{
  --blue:#0a5ea8;
  --blue-deep:#08518f;
  --blue-soft:#2d7fc4;
  --navy:#16324f;
  --ink:#333a42;
  --grey:#8a8f96;
  --light:#f3f5f8;
  --white:#ffffff;
  --foot-bar:#d9dadc;
}
*{margin:0;padding:0;box-sizing:border-box}
html,body{width:1200px;height:4147px;overflow:hidden}
body{font-family:"Open Sans",Arial,sans-serif;color:var(--ink);background:var(--white);position:relative}
.section{position:absolute;left:0;width:1200px}
.center{text-align:center}
.heading{font-family:"Raleway",Arial,sans-serif;font-weight:300;font-size:42px;letter-spacing:1px;color:var(--ink);text-align:center}
.heading strong{font-weight:700;color:var(--blue)}
.abs{position:absolute}

/* header */
.site-header{top:0;height:105px;background:var(--blue);z-index:3}
.nav-link{position:absolute;top:40px;font-family:"Raleway",sans-serif;font-weight:600;font-size:16px;color:var(--white);letter-spacing:.5px}
.brand{position:absolute;left:484px;top:0;width:229px;height:124px;background:var(--white);display:flex;align-items:center;justify-content:center;gap:12px;box-shadow:0 4px 10px rgba(0,0,0,.15)}
.brand-mark{width:34px;height:34px;background:var(--blue)}
.brand-name{font-family:"Raleway",sans-serif;font-weight:700;font-size:19px;line-height:1.15;color:var(--blue);letter-spacing:1px}

/* hero */
.hero{top:105px;height:572px;background:linear-gradient(135deg,#f4f4f2 0%,#dfe4e8 45%,#b9c7d3 100%)}
.hero-photo{position:absolute;inset:0}
.hero-arrow{position:absolute;top:250px}
.hero-title{position:absolute;left:503px;top:437px;font-family:"Raleway",sans-serif;font-weight:800;font-size:44px;color:var(--blue);letter-spacing:1px}
.hero-sub{position:absolute;left:503px;top:496px;width:630px;font-size:14px;font-style:italic;line-height:1.6;color:var(--blue-deep)}

/* welcome */
.welcome{top:677px;height:305px;background:var(--blue);color:var(--white)}
.welcome .heading{color:#b7cfe6;margin-top:52px}
.welcome .heading strong{color:var(--white)}
.welcome p{width:1000px;margin:24px auto 0;font-size:13.5px;line-height:2;text-align:center;color:#e2ecf6}

/* services */
.services{top:982px;height:663px}
.services .heading{margin-top:54px}
.service-card{position:absolute;top:132px;width:362px;height:468px;border:1px solid #dcdfe3;background:var(--white)}
.service-photo{height:240px}
.service-badge{position:absolute;left:157px;top:212px;width:48px;height:48px;background:var(--white);border-radius:50%;display:flex;align-items:center;justify-content:center}
.service-badge span{width:26px;height:26px;background:var(--blue)}
.service-card h3{margin-top:44px;text-align:center;font-family:"Raleway",sans-serif;font-weight:700;font-size:20px;color:var(--blue);letter-spacing:.5px}
.service-card p{width:300px;margin:12px auto 0;text-align:center;font-size:13.5px;line-height:1.9;color:var(--grey)}
.service-card svg{display:block;margin:18px auto 0}

/* why */
.why{top:1645px;height:415px;background:linear-gradient(180deg,#1d3a57 0%,#27496b 50%,#1b3550 100%)}
.why .heading{margin-top:96px;color:#b9c5d2}
.why p{margin-top:22px;text-align:center;font-size:16px;font-style:italic;line-height:1.9;color:var(--white)}
.call{position:absolute;left:322px;top:290px;display:flex;align-items:center;gap:20px;color:var(--white)}
.call-label{font-family:"Raleway",sans-serif;font-weight:700;font-size:30px}
.call-icon{width:66px;height:66px;border-radius:50%;background:var(--blue);display:flex;align-items:center;justify-content:center}
.call-number{font-family:"Raleway",sans-serif;font-weight:600;font-size:30px}

/* projects */
.projects{top:2060px;height:890px}
.projects .heading{margin-top:58px}
.projects .intro{width:900px;margin:20px auto 0;text-align:center;font-size:14px;line-height:1.9;color:var(--ink)}
.filter{position:absolute;top:199px}
.tile{position:absolute;width:333px;height:218px}
.tile-feature{background:var(--blue);color:var(--white);text-align:center}
.tile-feature h4{margin-top:38px;font-family:"Raleway",sans-serif;font-weight:700;font-size:20px}
.tile-feature p{width:270px;margin:10px auto 0;font-size:13.5px;line-height:1.7;color:#dce8f4}
.view-all{position:absolute;left:464px;top:769px}

/* clients */
.clients{top:2950px;height:415px;background:linear-gradient(135deg,#1f5f9c 0%,#2f78b8 50%,#1d5c98 100%)}
.clients .heading{margin-top:58px;color:#c6d9ec}
.clients .heading strong{color:var(--white)}
.quote-mark{width:90px;height:90px;border-radius:50%;background:var(--white);margin:28px auto 0;display:flex;align-items:center;justify-content:center}
.clients p{width:940px;margin:26px auto 0;text-align:center;font-size:14px;font-weight:600;line-height:1.9;color:var(--white)}
.client-name{margin-top:14px;text-align:center;font-family:"Raleway",sans-serif;font-weight:700;font-size:16px;color:var(--white)}
.client-arrow{position:absolute;top:168px}

/* news */
.news{top:3365px;height:368px}
.news .heading{margin-top:60px}
.news-item{position:absolute;top:155px;width:520px;height:158px}
.news-photo{position:absolute;left:0;top:0;width:186px;height:158px}
.news-body{position:absolute;left:200px;top:0;width:320px}
.news-body h4{font-family:"Raleway",sans-serif;font-weight:700;font-size:17px;line-height:1.35;color:var(--navy)}
.news-body p{margin-top:8px;font-size:13px;line-height:1.75;color:var(--grey)}
.news-date{margin-top:8px;display:flex;align-items:center;gap:8px;font-weight:700;font-size:15px;color:var(--blue)}

/* footer */
.site-footer{top:3733px;height:354px;background:var(--blue);color:var(--white)}
.foot-col{position:absolute;top:36px}
.foot-col h5{font-family:"Raleway",sans-serif;font-weight:700;font-size:17px;letter-spacing:.5px}
.foot-col ul{list-style:none;margin-top:22px}
.foot-col li{font-size:14px;line-height:33px;padding-left:22px;position:relative}
.foot-col li::before{content:"";position:absolute;left:0;top:14px;width:6px;height:6px;border-radius:50%;background:var(--white)}
.touch-row{display:flex;gap:14px;margin-top:18px;font-size:14px;line-height:1.6}
.social{display:flex;gap:12px;margin-top:22px}
.social span{width:34px;height:34px;border:1.5px solid var(--white);border-radius:50%}
.field{position:absolute;border:1px solid #7fb0dc;font-size:13px;color:#d6e6f4;padding:9px 10px}
.send{position:absolute;left:769px;top:265px}
.copyright{top:4087px;height:60px;background:var(--foot-bar);text-align:center;font-size:14px;line-height:60px;color:var(--ink)}
</style>
</head>
<body>

<header class="section site-header">
  <span class="nav-link" style="left:166px">HOME <svg width="12" height="8" viewBox="0 0 12 8"><path d="M0 0h12L6 8z" fill="#fff"/></svg></span>
  <span class="nav-link" style="left:271px">ABOUT</span>
  <span class="nav-link" style="left:368px">SERVICES</span>
  <div class="brand"><span class="brand-mark"></span><span class="brand-name">HARBOURLINE<br>HOMES</span></div>
  <span class="nav-link" style="left:760px">PROJECTS</span>
  <span class="nav-link" style="left:877px">NEWS</span>
  <span class="nav-link" style="left:954px">CONTACT</span>
  <svg class="abs" style="left:1060px;top:40px" width="20" height="20" viewBox="0 0 20 20"><circle cx="8" cy="8" r="6" fill="none" stroke="#fff" stroke-width="2.5"/><path d="M12.5 12.5L18 18" stroke="#fff" stroke-width="3"/></svg>
</header>

<section class="section hero">
  <div class="hero-photo" role="img" aria-label="Sketch of a two-storey white house turning into a finished home, framed by two hands"></div>
  <svg class="hero-arrow" style="left:26px" width="20" height="50" viewBox="0 0 20 50"><path d="M18 2L3 25l15 23" fill="none" stroke="#9aa4ad" stroke-width="2"/></svg>
  <svg class="hero-arrow" style="left:1150px" width="20" height="50" viewBox="0 0 20 50"><path d="M2 2l15 23L2 48" fill="none" stroke="#9aa4ad" stroke-width="2"/></svg>
  <div class="hero-title">WE BUILD YOUR DREAMS....</div>
  <p class="hero-sub">Lorem Ipsum is simply dummy text of the printing and typesetting industry. Lorem Ipsum has been the industry's standard dummy....</p>
</section>

<section class="section welcome">
  <h1 class="heading">WELCOME TO <strong>HARBOURLINE HOMES</strong></h1>
  <p>Lorem Ipsum is simply dummy text of the printing and typesetting industry. Lorem Ipsum has been the industry's standard dummy text ever since the 1500s, when an unknown printer took a galley of type and scrambled it to make a type specimen book. It has survived not only five centuries, but also the leap into electronic typesetting, remaining essentially unchanged. It was popularised in the 1960s with the release of Letraset sheets containing Lorem Ipsum passages, and more recently with desktop publishing software like Aldus</p>
  <svg class="abs" style="left:590px;top:278px" width="20" height="16" viewBox="0 0 20 16"><path d="M3 2l7 6 7-6M3 8l7 6 7-6" fill="none" stroke="#fff" stroke-width="2"/></svg>
</section>

<section class="section services">
  <h2 class="heading">SERVICES WE <strong>PROVIDE YOU</strong></h2>
  <article class="service-card" style="left:227px">
    <div class="service-photo" role="img" aria-label="Modern curved white residential house with glass facade" style="background:linear-gradient(180deg,#9fb7cf,#6e8a6a)"></div>
    <div class="service-badge"><span></span></div>
    <h3>RESIDENTIAL HOUSE</h3>
    <p>Lorem Ipsum is simply dummy text of the printing and typesetting industry. Lorem Ipsum has been the industry's standard dummy text ever since the 1500s, when an unknown printer.</p>
    <svg width="30" height="12" viewBox="0 0 30 12"><path d="M0 6h27M22 1l6 5-6 5" fill="none" stroke="#333" stroke-width="2"/></svg>
  </article>
  <article class="service-card" style="left:611px">
    <div class="service-photo" role="img" aria-label="Light commercial building with white upper storey and glass frontage" style="background:linear-gradient(180deg,#c7d4df,#8d969e)"></div>
    <div class="service-badge"><span></span></div>
    <h3>LIGHT COMMERCIAL</h3>
    <p>Lorem Ipsum is simply dummy text of the printing and typesetting industry. Lorem Ipsum has been the industry's standard dummy text ever since the 1500s, when an unknown printer.</p>
    <svg width="30" height="12" viewBox="0 0 30 12"><path d="M0 6h27M22 1l6 5-6 5" fill="none" stroke="#333" stroke-width="2"/></svg>
  </article>
</section>

<section class="section why" role="img" aria-label="Construction team inside a timber-framed building under a dark blue overlay">
  <h2 class="heading">WHY CHOOSE <strong>HARBOURLINE HOMES ?</strong></h2>
  <p>We Modeling Project Before Site Construction, Which Enable Both Client And Construction<br>Team To Visually Analysis Whole Project,</p>
  <div class="call">
    <span class="call-label">Call Us Today :</span>
    <span class="call-icon"><svg width="30" height="30" viewBox="0 0 24 24"><path d="M6.6 10.8a15 15 0 0 0 6.6 6.6l2.2-2.2a1 1 0 0 1 1-.25 11.4 11.4 0 0 0 3.6.57 1 1 0 0 1 1 1V20a1 1 0 0 1-1 1A17 17 0 0 1 3 4a1 1 0 0 1 1-1h3.5a1 1 0 0 1 1 1c0 1.25.2 2.45.57 3.57a1 1 0 0 1-.25 1z" fill="#fff"/></svg></span>
    <span class="call-number">123 456 7890</span>
  </div>
</section>

<section class="section projects">
  <h2 class="heading">LATEST <strong>PROJECTS</strong></h2>
  <p class="intro">Lorem Ipsum is simply dummy text of the printing and typesetting industry. Lorem Ipsum has been the industry's standard dummy text ever since the 1500s, when an unknown printer took</p>
  <svg class="filter" style="left:222px" width="120" height="52" viewBox="0 0 120 52"><polygon points="14,1 106,1 119,26 106,51 14,51 1,26" fill="#0a5ea8"/><text x="60" y="32" text-anchor="middle" font-family="Raleway,sans-serif" font-weight="600" font-size="16" fill="#fff">ALL</text></svg>
  <svg class="filter" style="left:355px" width="196" height="52" viewBox="0 0 196 52"><polygon points="14,1 182,1 195,26 182,51 14,51 1,26" fill="#fff" stroke="#0a5ea8" stroke-width="1.5"/><text x="98" y="32" text-anchor="middle" font-family="Raleway,sans-serif" font-weight="600" font-size="16" fill="#333">RESIDENTIAL</text></svg>
  <svg class="filter" style="left:569px" width="204" height="52" viewBox="0 0 204 52"><polygon points="14,1 190,1 203,26 190,51 14,51 1,26" fill="#fff" stroke="#0a5ea8" stroke-width="1.5"/><text x="102" y="32" text-anchor="middle" font-family="Raleway,sans-serif" font-weight="600" font-size="16" fill="#333">COMMERCIAL</text></svg>
  <svg class="filter" style="left:785px" width="194" height="52" viewBox="0 0 194 52"><polygon points="14,1 180,1 193,26 180,51 14,51 1,26" fill="#fff" stroke="#0a5ea8" stroke-width="1.5"/><text x="97" y="32" text-anchor="middle" font-family="Raleway,sans-serif" font-weight="600" font-size="16" fill="#333">INTERIOR DESIGN</text></svg>

  <div class="tile" style="left:77px;top:293px;background:linear-gradient(135deg,#c99a62,#7a5632)" role="img" aria-label="Couple reviewing plans inside a timber-framed room"></div>
  <div class="tile tile-feature" style="left:434px;top:293px">
    <h4>PROJECT TITLE</h4>
    <p>Lorem Ipsum is simply dummy text of the printing and typesetting industry is simply dummy text of the printing.</p>
    <svg style="margin-top:6px" width="30" height="12" viewBox="0 0 30 12"><path d="M0 6h27M22 1l6 5-6 5" fill="none" stroke="#fff" stroke-width="2"/></svg>
  </div>
  <div class="tile" style="left:788px;top:293px;background:linear-gradient(135deg,#e8e8e8,#6d6f72)" role="img" aria-label="Modern interior with white sofa and red accents"></div>
  <div class="tile" style="left:77px;top:531px;background:linear-gradient(180deg,#b9d3ea,#eef1f3)" role="img" aria-label="White modern house with palm trees"></div>
  <div class="tile" style="left:434px;top:531px;background:linear-gradient(135deg,#d6b284,#8b6a45)" role="img" aria-label="Family standing in a timber frame under construction"></div>
  <div class="tile" style="left:788px;top:531px;background:linear-gradient(180deg,#9fb2c2,#5e6b58)" role="img" aria-label="Grey two-storey family home with lawn"></div>

  <svg class="view-all" width="272" height="56" viewBox="0 0 272 56"><polygon points="16,1 256,1 271,28 256,55 16,55 1,28" fill="#0a5ea8"/><text x="136" y="34" text-anchor="middle" font-family="Raleway,sans-serif" font-weight="600" font-size="17" fill="#fff">VIEW ALL PROJECTS</text></svg>
</section>

<section class="section clients" role="img" aria-label="Mosaic of client portraits under a blue overlay">
  <h2 class="heading">OUR <strong>HAPPY CLIENT</strong></h2>
  <div class="quote-mark"><svg width="40" height="32" viewBox="0 0 40 32"><path d="M2 32V18C2 8 7 2 16 0l1 4c-5 2-7 6-7 10h7v18zM23 32V18c0-10 5-16 14-18l1 4c-5 2-7 6-7 10h7v18z" fill="#0a5ea8"/></svg></div>
  <p>Lorem Ipsum is simply dummy text of the printing and typesetting industry. Lorem Ipsum has been the industry's standard dummy text ever since the 1500s, when an unknown printer took a galley of type and scrambled it to make a type specimen book. It has survived not only five centuries, but also the leap into electronic.</p>
  <div class="client-name">— CLIENT NAME</div>
  <svg class="client-arrow" style="left:78px" width="20" height="50" viewBox="0 0 20 50"><path d="M18 2L3 25l15 23" fill="none" stroke="#fff" stroke-width="2"/></svg>
  <svg class="client-arrow" style="left:1100px" width="20" height="50" viewBox="0 0 20 50"><path d="M2 2l15 23L2 48" fill="none" stroke="#fff" stroke-width="2"/></svg>
</section>

<section class="section news">
  <h2 class="heading">LATEST <strong>NEWS</strong></h2>
  <article class="news-item" style="left:77px">
    <div class="news-photo" role="img" aria-label="Large new family house with front lawn" style="background:linear-gradient(180deg,#c3d4e2,#8a7b66)"></div>
    <div class="news-body">
      <h4>Lorem Ipsum is the simply dummy text of the printing and ?</h4>
      <p>Lorem Ipsum is simply dummy text of the printing and typesetting industry Lorem Ipsum has been the industry's...</p>
      <div class="news-date"><svg width="16" height="16" viewBox="0 0 16 16"><rect x="1" y="3" width="14" height="12" fill="none" stroke="#0a5ea8" stroke-width="2"/><path d="M1 7h14M5 1v4M11 1v4" stroke="#0a5ea8" stroke-width="2"/></svg>06 Nov 2017</div>
    </div>
  </article>
  <article class="news-item" style="left:617px">
    <div class="news-photo" role="img" aria-label="Builder in hard hat at a timber frame site" style="background:linear-gradient(135deg,#e3b874,#8c6a3f)"></div>
    <div class="news-body">
      <h4>Lorem Ipsum is the simply dummy text of the printing and ?</h4>
      <p>Lorem Ipsum is simply dummy text of the printing and typesetting industry Lorem Ipsum has been the industry's...</p>
      <div class="news-date"><svg width="16" height="16" viewBox="0 0 16 16"><rect x="1" y="3" width="14" height="12" fill="none" stroke="#0a5ea8" stroke-width="2"/><path d="M1 7h14M5 1v4M11 1v4" stroke="#0a5ea8" stroke-width="2"/></svg>06 Nov 2017</div>
    </div>
  </article>
</section>

<footer class="section site-footer">
  <div class="foot-col" style="left:77px">
    <h5>SERVICES</h5>
    <ul><li>Home</li><li>About</li><li>Services</li><li>Projects</li><li>News</li><li>Contact</li></ul>
  </div>
  <div class="foot-col" style="left:265px">
    <h5>SERVICES</h5>
    <ul><li>Residential House</li><li>light commercial</li><li>Interior Design</li></ul>
  </div>
  <div class="foot-col" style="left:489px;width:250px">
    <h5>GET IN TOUCH</h5>
    <div class="touch-row"><svg width="16" height="22" viewBox="0 0 16 22"><path d="M8 0a8 8 0 0 0-8 8c0 6 8 14 8 14s8-8 8-14a8 8 0 0 0-8-8z" fill="#fff"/><circle cx="8" cy="8" r="3" fill="#0a5ea8"/></svg><span><b>HARBOURLINE HOMES</b><br>101 - Lorem Ipsum Is Simple<br>Dummy Text of Print</span></div>
    <div class="touch-row"><svg width="18" height="18" viewBox="0 0 24 24"><path d="M6.6 10.8a15 15 0 0 0 6.6 6.6l2.2-2.2a1 1 0 0 1 1-.25 11.4 11.4 0 0 0 3.6.57 1 1 0 0 1 1 1V20a1 1 0 0 1-1 1A17 17 0 0 1 3 4a1 1 0 0 1 1-1h3.5a1 1 0 0 1 1 1c0 1.25.2 2.45.57 3.57a1 1 0 0 1-.25 1z" fill="#fff"/></svg><span>+123 456 4890</span></div>
    <div class="touch-row"><svg width="18" height="14" viewBox="0 0 18 14"><rect width="18" height="14" fill="#fff"/><path d="M0 0l9 7 9-7" fill="none" stroke="#0a5ea8" stroke-width="1.5"/></svg><span>info@harbourlinehomes.com</span></div>
    <div class="social" style="margin-left:0"><span></span><span></span><span></span></div>
  </div>
  <div class="foot-col" style="left:769px"><h5>CONTACT US</h5></div>
  <div class="field" style="left:769px;top:91px;width:167px;height:39px">Name*</div>
  <div class="field" style="left:946px;top:91px;width:177px;height:39px">Email*</div>
  <div class="field" style="left:769px;top:138px;width:354px;height:39px">Subject*</div>
  <div class="field" style="left:769px;top:188px;width:354px;height:66px">Message*</div>
  <svg class="send" width="116" height="46" viewBox="0 0 116 46"><polygon points="14,1 102,1 115,23 102,45 14,45 1,23" fill="#fff"/><text x="58" y="29" text-anchor="middle" font-family="Raleway,sans-serif" font-weight="700" font-size="16" fill="#0a5ea8">ALL</text></svg>
</footer>

<div class="section copyright">©HARBOURLINE HOMES- 2017. All Rights Reserved.</div>

</body>
</html>
```